Modern Retail Coffee Label for established Roastery! 17 years!

We are looking for a Retail Coffee Bag Label... JUST THE LABEL TO GO ON AN EXISTING BAG. Our current label is provided and our Logo.. we have had the same Red Bags FOREVER so we are looking for a label to compliment that tradition and to be placed on the bags we have used for 17 years.

We have a retail line of bags with locally roasted coffee. Our business has been around 17years and is in need of a design upgrade! We have a red coffee bag and are looking for a sleek modern label. I will attach a file of our label right now so you can see what it looks like. We are just looking for a more modern version. a few inclusions:

Locally Roasted
100% Arabica Coffee
Heron Kin's Coffee
heronkincoffee.example
logo

The black label with the red and yellow color label is the old one... the new label should be the White background and black border one...

Target Market(s)

Retail Coffee Consumers

Font styles to use
Other font styles liked:
• use what you think. we are located in SW Wisconsin but ship coffee EVERYWHERE

Colors

Designer to choose only greyscale colors for use in the design.

Requirements
Must have
• Locally Roasted (Platteville,WI)
• 100% Arabica Coffee
• heronkincoffee.example
• logo
Nice to have
• Badgers
• "Since 2003"
Should not have
• Any lunabrew or big brand themes

```html
<!DOCTYPE html>
<html lang="en">
<head>
<meta charset="utf-8">
<title>Heron Kin's Coffee — Retail Label</title>
<link href="https://fonts.googleapis.com/css2?family=Montserrat:wght@300;700;800&family=Kaushan+Script&display=swap" rel="stylesheet">
<style>
  :root {
    --ink: #0d0d0d;
    --bean-dark: #161616;
    --bean-mid: #3a3a3a;
    --paper: #ffffff;
    --rule: #1a1a1a;
    --text-light: #ffffff;
    --text-dark: #1b1b1b;
  }
  html, body {
    margin: 0;
    padding: 0;
    overflow: hidden;
    background: var(--paper);
  }
  .label {
    position: relative;
    width: 960px;
    height: 1200px;
    overflow: hidden;
    background: var(--paper);
    font-family: "Montserrat", sans-serif;
  }
  .bean-field {
    position: absolute;
    left: 0; top: 0;
    width: 960px; height: 980px;
    background: radial-gradient(ellipse at 50% 45%, var(--bean-mid) 0%, var(--bean-dark) 70%, var(--ink) 100%);
  }
  .since {
    position: absolute;
    top: 38px; left: 0; width: 960px;
    line-height: 36px;
    text-align: center;
    color: var(--text-light);
    font-weight: 700;
    font-size: 32px;
    letter-spacing: 7px;
  }
  .brand-name {
    margin: 0;
    color: var(--text-light);
    font-weight: 800;
  }
  .brand-name .line {
    position: absolute;
    left: 0; width: 960px;
    text-align: center;
    font-size: 100px;
    line-height: 100px;
    letter-spacing: 1px;
  }
  .brand-name .line-1 { top: 148px; }
  .brand-name .line-2 { top: 392px; letter-spacing: 3px; }
  .tagline {
    position: absolute;
    top: 576px; left: 0; width: 960px;
    text-align: center;
    color: var(--text-light);
    font-weight: 700;
    font-size: 50px;
    line-height: 80px;
    letter-spacing: 12px;
    margin: 0;
  }
  .promise {
    position: absolute;
    top: 795px; left: 0; width: 960px;
    text-align: center;
    color: var(--text-light);
    font-family: "Kaushan Script", cursive;
    font-size: 102px;
    line-height: 1.1;
    margin: 0;
  }
  .facts {
    position: absolute;
    left: 50px; top: 1005px;
    margin: 0; padding: 0;
    list-style: none;
    color: var(--text-dark);
    font-weight: 300;
    font-size: 23px;
    letter-spacing: 5px;
    line-height: 50px;
  }
  .facts-rule {
    position: absolute;
    left: 50px; top: 1116px;
    width: 640px; height: 0;
    border-top: 1.5px solid var(--rule);
  }
  .web {
    position: absolute;
    left: 50px; top: 1142px;
    line-height: 24px;
    color: var(--text-dark);
    font-weight: 700;
    font-size: 20px;
    letter-spacing: 7px;
  }
  .paw-mark {
    position: absolute;
    left: 752px; top: 920px;
    width: 196px; height: 272px;
    border-radius: 40px;
    background: linear-gradient(160deg, #2a2a2a, var(--ink));
  }
</style>
</head>
<body>
<main class="label">
  <div class="bean-field" role="img" aria-label="Close-up photograph of dark roasted coffee beans in greyscale"></div>

  <div class="since">SINCE 2003</div>

  <h1 class="brand-name">
    <span class="line line-1">HERON KIN'S</span>
    <span class="line line-2">COFFEE</span>
  </h1>

  <p class="tagline">EXPERIENCE<br>THE DIFFERENCE</p>

  <p class="promise">fresher. Smoother.</p>

  <ul class="facts">
    <li>100% ARABICA COFFEE</li>
    <li>LOCALLY ROASTED IN PLATTEVILLE, WI</li>
  </ul>
  <div class="facts-rule"></div>
  <div class="web">HERONKINCOFFEE.EXAMPLE</div>

  <div class="paw-mark" role="img" aria-label="Black animal paw print illustration with claw marks"></div>
</main>
</body>
</html>
```